Business Card Design

Business card design.

Business card is to have logo, website address and email address.

Website is www.brightkettle.ie
Email is info@brightkettle.ie
Logo uploaded

I have ordered Business Card Printing via Print Harbor, the Double-sided colour printed option with gloss finish.

Industry/Entity Type

Business

```html
<!DOCTYPE html>
<html lang="en">
<head>
<meta charset="utf-8">
<title>BrightKettle.ie — Business Card</title>
<link rel="stylesheet" href="https://fonts.googleapis.com/css2?family=Questrial&display=swap">
<style>
  :root {
    --backdrop: #ece7e1;
    --card-peach: #fbcb9e;
    --brand-red: #d1282a;
    --ink-dark: #1c1c1c;
    --card-shadow: 0 10px 28px rgba(60, 40, 20, 0.22);
  }
  * { box-sizing: border-box; margin: 0; padding: 0; }
  html, body {
    width: 1200px;
    height: 901px;
    overflow: hidden;
    background: var(--backdrop);
    font-family: "Questrial", "Century Gothic", sans-serif;
  }
  .sheet {
    width: 1200px;
    height: 901px;
    display: flex;
    align-items: center;
    justify-content: center;
    gap: 60px;
  }
  .card {
    position: relative;
    width: 525px;
    height: 300px;
    background: var(--card-peach);
    box-shadow: var(--card-shadow);
    overflow: hidden;
  }

  /* Front: red panel with wordmark and contact details */
  .card-front .red-panel {
    position: absolute;
    left: 0; top: 0;
    width: 232px;
    height: 100%;
    background: var(--brand-red);
  }
  .card-front .wordmark-tab {
    position: absolute;
    left: 0;
    top: 168px;
    height: 46px;
    padding: 0 18px 0 22px;
    background: var(--brand-red);
    display: flex;
    align-items: center;
    gap: 10px;
  }
  .card-front .wordmark {
    color: var(--card-peach);
    font-size: 34px;
    letter-spacing: 0.5px;
    line-height: 1;
  }
  .card-front .wordmark-dot {
    width: 12px; height: 12px;
    border-radius: 50%;
    background: var(--card-peach);
  }
  .card-front .contact {
    position: absolute;
    left: 22px;
    color: var(--card-peach);
    font-size: 22px;
    letter-spacing: 0.3px;
  }
  .card-front .contact-email { top: 226px; }
  .card-front .contact-web { top: 258px; }

  /* Back: centred wordmark with red side strip */
  .card-back .side-strip {
    position: absolute;
    right: 0; top: 0;
    width: 58px;
    height: 100%;
    background: var(--brand-red);
    display: flex;
    align-items: center;
    justify-content: center;
  }
  .card-back .side-web {
    color: var(--card-peach);
    font-size: 21px;
    letter-spacing: 0.5px;
    writing-mode: vertical-rl;
    white-space: nowrap;
  }
  .card-back .logo-lockup {
    position: absolute;
    left: 0; right: 58px;
    top: 0; bottom: 0;
    display: flex;
    flex-direction: column;
    align-items: center;
    justify-content: center;
    gap: 14px;
  }
  .card-back .logo-circle {
    width: 44px; height: 44px;
    border-radius: 50%;
    background: var(--brand-red);
  }
  .card-back .logo-name {
    color: var(--ink-dark);
    font-size: 42px;
    letter-spacing: 1px;
    line-height: 1;
  }
</style>
</head>
<body>
  <main class="sheet">
    <section class="card card-front" aria-label="Business card front">
      <div class="red-panel"></div>
      <div class="wordmark-tab">
        <span class="wordmark">BRIGHTKETTLE.IE</span>
        <span class="wordmark-dot"></span>
      </div>
      <p class="contact contact-email">info@brightkettle.ie</p>
      <p class="contact contact-web">www.brightkettle.ie</p>
    </section>

    <section class="card card-back" aria-label="Business card back">
      <div class="logo-lockup">
        <span class="logo-circle"></span>
        <span class="logo-name">BRIGHTKETTLE.IE</span>
      </div>
      <div class="side-strip">
        <span class="side-web">www.brightkettle.ie</span>
      </div>
    </section>
  </main>
</body>
</html>
```